Summer Music/Chorus/Choir Camp for Young Singers Ages 8-13

We need a flyer for a summer camp for young singers ages 8-13. We are nonprofit community children's chorus in Miami, FL. Our camp provides specialized training in music theory, sight-reading,and aural training through daily choral rehearsals in an environment that is both positive and a lot of fun! Our camp offers children the opportunity to come as they are, no matter the level of experience, and grow tremendously in their musicianship skills. In addition to this, our campers participate in song-writing, masterclasses, community performances, and media projects. The final design should be clean, fun, not too crowded, should appeal to boys and girls ages 8-13, and something someone that age would consider "cool" and not too childish. Drawings are cool, something different.
Updates

Target Market(s)

Ages 8-13 and parents of those kids.

Industry/Entity Type

Community

Requirements
Must have
• All info attached.
Nice to have
• Things that relate to music, especially related to singing/choirs
Should not have
• instruments, stock photos of children, or photos from our website (unless they are used very creatively), or photos in general. I've attached our previous camp flyer and our current organization flyer but I don't necessarily want this flyer to look like those.

```html
<!DOCTYPE html>
<html lang="en">
<head>
<meta charset="utf-8">
<title>Summer Camp 2016 – Bright Notes Youth Chorus</title>
<link rel="stylesheet" href="https://fonts.googleapis.com/css2?family=Oswald:wght@400;500&family=Roboto+Condensed:wght@400;700&family=Roboto:ital,wght@0,300;0,400;1,300&display=swap">
<style>
  :root {
    --page: #ffffff;
    --teal: #1aa89b;
    --logo-teal: #3f7d78;
    --grey-head: #666a6d;
    --body-grey: #6b6b6b;
    --ink: #2f3336;
    --note-top: #62cde1;
    --note-bottom: #2f98b3;
    --pin: #6dbf3a;
    --badge: #2b2b2b;
  }
  * { margin: 0; padding: 0; box-sizing: border-box; }
  html, body { width: 1006px; height: 1200px; overflow: hidden; background: var(--page); }
  .flyer { position: relative; width: 1006px; height: 1200px; background: var(--page); overflow: hidden; }

  .camp-title {
    position: absolute; top: 40px; left: 24px; width: 1006px;
    text-align: center; font-family: "Oswald", sans-serif; font-weight: 500;
    font-size: 100px; line-height: 1; color: var(--teal); letter-spacing: -3px;
  }
  .camp-tagline {
    position: absolute; top: 150px; left: 24px; width: 1006px;
    text-align: center; font-family: "Oswald", sans-serif; font-weight: 400;
    font-size: 35px; line-height: 1; color: var(--grey-head); letter-spacing: -0.5px;
  }

  .colour-band {
    position: absolute; left: 0; top: 200px; width: 100%; height: 380px;
    background:
      linear-gradient(to bottom, rgba(255,255,255,0.1), rgba(255,255,255,0.95)),
      linear-gradient(90deg, #f4a3a8 0%, #f7c98f 25%, #eef0a2 45%, #bfe7d6 65%, #d9c9ea 85%, #c7dff2 100%);
    opacity: 0.75;
  }

  .camp-illustration {
    position: absolute; left: 110px; top: 228px; width: 790px; height: 300px;
    border-radius: 24px;
    background: radial-gradient(ellipse at 50% 45%, rgba(26,168,155,0.28), rgba(63,125,120,0.12) 60%, rgba(255,255,255,0) 100%);
  }

  .chorus-name {
    position: absolute; left: 30px; top: 552px; display: flex; align-items: center; gap: 16px;
  }
  .chorus-name__dot { width: 32px; height: 32px; border-radius: 50%; background: var(--logo-teal); }
  .chorus-name__text {
    font-family: "Oswald", sans-serif; font-weight: 500; font-size: 68px; line-height: 1;
    color: var(--logo-teal);
  }

  .info-note {
    position: absolute; left: 548px; top: 625px; width: 410px; height: 390px;
    background: linear-gradient(to bottom, var(--note-top), var(--note-bottom));
    transform: rotate(-3deg);
    box-shadow: 2px 6px 8px rgba(0,0,0,0.3);
    font-family: "Roboto Condensed", sans-serif; color: var(--ink); text-align: center;
    padding: 108px 20px 0;
  }
  .info-note__dates { font-size: 30px; font-weight: 700; }
  .info-note__extra { font-size: 17px; margin-top: 4px; line-height: 1.35; }
  .info-note__venue { font-size: 22px; margin-top: 30px; line-height: 1.2; }
  .push-pin { position: absolute; left: 190px; top: -15px; }

  .camp-description {
    position: absolute; left: 38px; top: 806px; width: 428px;
    font-family: "Roboto", sans-serif; font-weight: 300; font-size: 17.5px; line-height: 24.2px;
    color: var(--body-grey); text-align: justify; hyphens: auto;
  }
  .nonprofit-note {
    position: absolute; left: 20px; top: 1060px; width: 468px; text-align: center;
    font-family: "Roboto", sans-serif; font-style: italic; font-weight: 300; font-size: 15px;
    line-height: 1.2; color: var(--body-grey);
  }
  .partners { position: absolute; left: 32px; top: 1124px; display: flex; align-items: center; gap: 22px; }
  .partner-badge { background: var(--badge); }
  .partner-badge--wide { width: 100px; height: 44px; border-radius: 0 22px 22px 0; }
  .partner-badge--square { width: 46px; height: 48px; background: none; border: 3px solid var(--badge); }
  .partner-badge--bar { width: 210px; height: 28px; border-radius: 3px; }

  .contact { position: absolute; left: 560px; top: 1058px; width: 400px; text-align: center; font-style: normal; }
  .contact__phone {
    display: flex; align-items: center; justify-content: center; gap: 14px;
    font-family: "Roboto", sans-serif; font-weight: 400; font-size: 44px; color: var(--ink); letter-spacing: 1px;
  }
  .contact__line {
    font-family: "Roboto", sans-serif; font-weight: 400; font-size: 23px; line-height: 27px; color: var(--ink);
  }
</style>
</head>
<body>
<main class="flyer">
  <h1 class="camp-title">SUMMER CAMP 2016</h1>
  <p class="camp-tagline">MUSIC ★ CHORUS ★ CHOIR</p>

  <div class="colour-band" role="img" aria-label="Soft pastel mosaic of coloured squares"></div>
  <div class="camp-illustration" role="img" aria-label="Hand-drawn illustration of young singers in a choir with music notes floating around them"></div>

  <div class="chorus-name">
    <span class="chorus-name__dot"></span>
    <p class="chorus-name__text">Bright Notes<br>Youth Chorus</p>
  </div>

  <section class="info-note">
    <svg class="push-pin" width="40" height="70" viewBox="0 0 40 70" aria-hidden="true">
      <line x1="20" y1="40" x2="22" y2="68" stroke="#888" stroke-width="3"/>
      <rect x="12" y="14" width="16" height="20" rx="3" fill="var(--pin)"/>
      <ellipse cx="20" cy="12" rx="13" ry="9" fill="var(--pin)"/>
      <ellipse cx="20" cy="38" rx="17" ry="7" fill="var(--pin)"/>
    </svg>
    <p class="info-note__dates">July 18-29, 9am-3pm (M-F)*</p>
    <p class="info-note__extra">*Extended hours available (7:30am-5:30pm)<br>for an extra $50 per week.</p>
    <p class="info-note__venue">Bayside Community Arts Hall,<br>4200 SW 180th Street<br>Miami, FL 33157</p>
  </section>

  <p class="camp-description">Youth and children who love to sing will have a blast at our choral camp! Our music educators and industry professionals are dedicated to enhancing the lives of young singers through choral training which develops vocal technique, ear-training, music reading, and interpersonal skills. Activities are fun and interactive and former music training is not necessary. Singers in grades 3-9 are invited to attend! Register today!</p>

  <p class="nonprofit-note">Bright Notes is a 501 (c)(3) Nonprofit organization.<br>Donations made to BNYC are tax-exempt</p>

  <div class="partners" aria-label="Partner organisations">
    <span class="partner-badge partner-badge--wide"></span>
    <span class="partner-badge partner-badge--square"></span>
    <span class="partner-badge partner-badge--bar"></span>
  </div>

  <address class="contact">
    <p class="contact__phone">
      <svg width="42" height="42" viewBox="0 0 42 42" aria-hidden="true">
        <circle cx="21" cy="21" r="18.5" fill="none" stroke="var(--ink)" stroke-width="3"/>
        <path d="M14 11c1.5-1 3-1 3.6.2l2 4c.5 1 0 2-.8 2.6l-1.3 1c1 2.3 2.8 4.2 5 5.4l1.1-1.2c.7-.8 1.700-1.1 2.6-.6l3.8 2.2c1.1.7 1 2.2 0 3.5-1.3 1.6-3.3 2.3-5.4 1.5C18.5 27.6 14 23 12 17.6c-.7-2.3 0-4.9 2-6.6z" fill="var(--ink)"/>
      </svg>
      305.555.0142
    </p>
    <p class="contact__line">info@brightnoteschorus.org</p>
    <p class="contact__line">brightnoteschorus.org</p>
  </address>
</main>
</body>
</html>
```